Wine Bottle Label Logo Design

My fiancé and I are getting married in September and we made homemade wine which will be given to the guests as a wedding favor. We need label/logo for our wine bottles. We were looking for something rustic yet modern and simple. We had an idea for beige and cranberry colored wine stained, weathered, imperfect heart. Things that will need to be incorporated into the label design are as follows:
Our last name and also the name of the wine: Fusaldi
The year: 2012
Where is says Alcohol Content on a wine bottle normally write: Alcohol: Deceiving% by vol.
Type of wine: Red Wine
Incorporate our wedding date: Foot Stomped and Bottled for Nadia and Gus's Wedding Day 9/28/13
Wedding

```html
<!DOCTYPE html>
<html lang="en">
<head>
<meta charset="utf-8">
<title>Fusaldi Wedding Wine Label</title>
<link rel="stylesheet" href="https://fonts.googleapis.com/css2?family=Playfair+Display:ital,wght@0,700;0,900;1,700&family=PT+Sans:wght@400;700&display=swap">
<style>
  :root {
    --backdrop: #3a3a3a;
    --cranberry: #b81f3a;
    --cranberry-deep: #8e1427;
    --ribbon-dark: #6e0f18;
    --gold: #c8a05a;
    --gold-light: #e8cf94;
    --beige: #f1dfb2;
    --beige-dark: #d9bf84;
    --brown: #4a3018;
    --wine-text: #8a1020;
    --cream-text: #f3d9a0;
  }
  html, body {
    margin: 0;
    padding: 0;
    overflow: hidden;
  }
  .canvas {
    width: 1200px;
    height: 1000px;
    background: linear-gradient(180deg, #6a6a6a 0%, var(--backdrop) 100%);
    display: flex;
    align-items: center;
    justify-content: center;
    overflow: hidden;
  }
  .wine-label {
    width: 552px;
    height: 897px;
    display: block;
  }
  .label-mark { fill: none; stroke: var(--brown); stroke-width: 1.4; }
  .alcohol-line { font-family: "PT Sans", sans-serif; font-weight: 700; font-size: 5.2px; fill: var(--brown); }
  .edition-line { font-family: "PT Sans", sans-serif; font-weight: 700; font-size: 7px; fill: var(--wine-text); }
  .wine-name { font-family: "Playfair Display", serif; font-weight: 900; font-size: 34px; fill: #a8793a; letter-spacing: -0.5px; }
  .dedication { font-family: "PT Sans", sans-serif; font-size: 6px; fill: var(--brown); }
  .wine-type { font-family: "Playfair Display", serif; font-style: italic; font-weight: 700; font-size: 11px; fill: var(--wine-text); }
  .wedding-date { font-family: "PT Sans", sans-serif; font-size: 9px; fill: var(--cream-text); letter-spacing: 0.3px; }
</style>
</head>
<body>
<main class="canvas">
  <svg class="wine-label" viewBox="0 0 240 390" xmlns="http://www.w3.org/2000/svg" aria-labelledby="label-title">
    <title id="label-title">Fusaldi 2012 Edition red wine label</title>
    <defs>
      <linearGradient id="cranberry-fill" x1="0" y1="0" x2="1" y2="1">
        <stop offset="0" stop-color="#c72a45"/>
        <stop offset="1" stop-color="var(--cranberry-deep)"/>
      </linearGradient>
      <linearGradient id="beige-fill" x1="0" y1="0" x2="0" y2="1">
        <stop offset="0" stop-color="#f6e8c4"/>
        <stop offset="1" stop-color="var(--beige-dark)"/>
      </linearGradient>
      <linearGradient id="banner-fill" x1="0" y1="0" x2="0" y2="1">
        <stop offset="0" stop-color="var(--gold-light)"/>
        <stop offset="1" stop-color="#b98d47"/>
      </linearGradient>
      <path id="date-arc" d="M40,262 Q120,318 200,262"/>
    </defs>

    <!-- hanging ribbon tail -->
    <path class="ribbon-tail" d="M88,240 L145,240 L145,385 L116.5,355 L88,385 Z" fill="var(--ribbon-dark)" stroke="#4d0a10" stroke-width="0.8"/>

    <!-- crest-shaped label body -->
    <path class="label-frame" d="M20,28 Q120,-6 220,28 L220,42 Q235,48 235,64 L235,245 Q235,256 222,262 Q180,316 120,319 Q60,316 18,262 Q5,256 5,245 L5,64 Q5,48 20,42 Z" fill="var(--gold)"/>
    <path class="label-body" d="M23,32 Q120,0 217,32 L217,45 Q231,51 231,66 L231,243 Q231,253 219,259 Q178,311 120,314 Q62,311 21,259 Q9,253 9,243 L9,66 Q9,51 23,45 Z" fill="url(#cranberry-fill)"/>

    <!-- diamond panel -->
    <path class="diamond-frame" d="M120,30 L233,155 L120,280 L7,155 Z" fill="var(--gold)"/>
    <path class="diamond-edge" d="M120,34 L229,155 L120,276 L11,155 Z" fill="var(--brown)"/>
    <path class="diamond-panel" d="M120,37 L226,155 L120,273 L14,155 Z" fill="url(#beige-fill)"/>

    <!-- couple's mark placeholder -->
    <circle class="label-mark" cx="120" cy="70" r="8"/>

    <text class="alcohol-line" x="120" y="94" text-anchor="middle">Deceiving% by vol.</text>
    <text class="edition-line" x="120" y="113" text-anchor="middle">2012 EDITION</text>
    <text class="wine-name" x="120" y="164" text-anchor="middle">Fusaldi</text>
    <text class="dedication" x="120" y="195" text-anchor="middle">Foot Stomped and Bottled</text>
    <text class="dedication" x="120" y="203" text-anchor="middle">for Nadia and Gus's</text>

    <!-- wine type banner -->
    <path class="banner-ends" d="M50,222 L70,226 L70,246 L50,250 L58,236 Z M190,222 L170,226 L170,246 L190,250 L182,236 Z" fill="#9a6f32"/>
    <path class="banner" d="M62,220 Q120,232 178,220 L178,244 Q120,256 62,244 Z" fill="url(#banner-fill)" stroke="#8a5f28" stroke-width="0.8"/>
    <text class="wine-type" x="120" y="242" text-anchor="middle">Red Wine</text>

    <text class="wedding-date"><textPath href="#date-arc" startOffset="50%" text-anchor="middle">Wedding Day 9/28/13</textPath></text>
  </svg>
</main>
</body>
</html>
```